Quillory Nest Business Card

I need a business card design. We are a collaborate online training company. Our colors are gray and green. Our website is QuilloryNest.com

I would like an area for a profile picture within the card

```html
<!DOCTYPE html>
<html lang="en">
<head>
<meta charset="utf-8">
<title>Quillory Nest Business Card</title>
<link href="https://fonts.googleapis.com/css2?family=Source+Sans+3:wght@400;600;700&display=swap" rel="stylesheet">
<style>
  :root {
    --bg-top: #2a2a2a;
    --bg-bottom: #040404;
    --card: #cacaca;
    --ink: #2a2a2a;
    --ink-soft: #6f6f6f;
    --green: #8cc63f;
    --photo-light: #b9b4ae;
    --photo-dark: #3a3a3e;
  }
  * { margin: 0; padding: 0; box-sizing: border-box; }
  html, body { width: 1200px; height: 900px; overflow: hidden; }
  body {
    position: relative;
    background: linear-gradient(180deg, var(--bg-top) 0%, #1a1a1a 50%, var(--bg-bottom) 100%);
    font-family: "Source Sans 3", Arial, sans-serif;
  }
  .card {
    position: absolute;
    top: 306px;
    width: 439px;
    height: 271px;
    background: var(--card);
    border-radius: 10px;
    overflow: hidden;
  }
  .card--front { left: 149px; }
  .card--back { left: 608px; width: 441px; }

  .profile-photo {
    position: absolute;
    left: 0;
    top: 38px;
    width: 220px;
    height: 233px;
    background:
      radial-gradient(ellipse 38% 30% at 55% 35%, var(--photo-light) 0%, rgba(185,180,174,0) 100%),
      linear-gradient(180deg, rgba(202,202,202,0) 0%, rgba(202,202,202,0) 45%, var(--photo-dark) 75%, #222 100%);
  }

  .details {
    position: absolute;
    left: 252px;
    top: 41px;
    color: var(--ink-soft);
    font-size: 12.5px;
    line-height: 16px;
  }
  .details__name {
    color: var(--ink);
    font-size: 16px;
    font-weight: 600;
    line-height: 20px;
  }
  .details__role { margin-bottom: 22px; }
  .details__address { margin-bottom: 26px; }
  .contact-list { list-style: none; }
  .contact-list li {
    display: flex;
    align-items: center;
    height: 16px;
  }
  .contact-list svg {
    width: 9px;
    height: 9px;
    margin-right: 8px;
    margin-left: 1px;
    fill: var(--ink);
  }

  .brand {
    position: absolute;
    left: 0;
    right: 0;
    top: 104px;
    display: flex;
    align-items: center;
    justify-content: center;
    gap: 12px;
  }
  .brand__dot {
    width: 34px;
    height: 34px;
    border-radius: 50%;
    background: var(--green);
  }
  .brand__name {
    font-size: 36px;
    font-weight: 700;
    color: var(--ink);
    letter-spacing: -0.5px;
    line-height: 1;
  }
</style>
</head>
<body>
  <section class="card card--front">
    <div class="profile-photo" role="img" aria-label="Profile photo of the managing director"></div>
    <div class="details">
      <p class="details__name">Dorian Vale</p>
      <p class="details__role">Managing Director</p>
      <p class="details__address">12345, Address Goes Here<br>Country Name, 123456.</p>
      <ul class="contact-list">
        <li><svg viewBox="0 0 10 10" aria-hidden="true"><path d="M2 0.5l2 2-1 1.2c.6 1.3 1.6 2.3 2.9 2.9l1.2-1 2 2-1.3 1.9C4.5 9.2 0.8 5.5 0.5 1.8z"/></svg>044-555 012 347</li>
        <li><svg viewBox="0 0 10 10" aria-hidden="true"><path d="M2 0h5v3H2zM0 3.5h10V8H8v2H2V8H0zM3 6.5v2.5h4V6.5z"/></svg>044-555 012 348</li>
        <li><svg viewBox="0 0 10 10" aria-hidden="true"><path d="M0 2h10v1L5 6 0 3zM0 4.2l5 3 5-3V8H0z"/></svg>hello@quillorynest.com</li>
        <li><svg viewBox="0 0 10 10" aria-hidden="true"><circle cx="5" cy="5" r="4.6"/></svg>www.quillorynest.com</li>
      </ul>
    </div>
  </section>

  <section class="card card--back">
    <div class="brand">
      <span class="brand__dot"></span>
      <span class="brand__name">Quillory Nest</span>
    </div>
  </section>
</body>
</html>
```